Coralvale Meat Traders Business Cards

We require business cards revamped with our logo. A few details we would like to use.

1. Round Edges
2. Our logo over the top of a wagyu cattle background photo on one side of the card

Other side of the card has the below details.

1. Person Name (First & Last)
2. Job Position
3. Mobile Number
4. Email Address
5. Website Address

Simple & Neat.

Target Market(s)

Sales

Industry/Entity Type

Agriculture

Contact Information for Business Card

CORALVALE MEAT TRADERS

Colors

Designer to choose colors to be used in the design.

Requirements
Must have
• Company Logo

```html
<!DOCTYPE html>
<html lang="en">
<head>
<meta charset="utf-8">
<title>Coralvale Meat Traders Business Cards</title>
<link href="https://fonts.googleapis.com/css2?family=Montserrat:wght@400;500;700&display=swap" rel="stylesheet">
<style>
  :root {
    --backdrop: #1f1f1f;
    --maroon: #650d25;
    --maroon-soft: #8a2d4b;
    --brand: #6b0f2a;
    --accent: #8b1a1a;
    --ink: #333333;
    --paper: #ffffff;
  }
  * { margin: 0; padding: 0; box-sizing: border-box; }
  html, body {
    width: 1200px; height: 1059px; overflow: hidden;
    background: var(--backdrop);
    font-family: 'Montserrat', sans-serif;
  }
  .canvas { position: relative; width: 1200px; height: 1059px; }
  .card { position: absolute; border-radius: 20px; overflow: hidden; }
  .card-front {
    left: 256px; top: 89px; width: 689px; height: 390px;
    background: var(--maroon);
  }
  .front-brand {
    position: absolute; left: 0; right: 0; top: 168px;
    text-align: center;
    font-weight: 700; font-size: 44px; letter-spacing: 1px;
    color: var(--maroon-soft);
  }
  .card-back {
    left: 252px; top: 546px; width: 696px; height: 395px;
    background: var(--paper);
  }
  .back-brand {
    position: absolute; left: 52px; top: 177px; width: 310px;
    font-weight: 700; font-size: 24px; color: var(--brand);
    white-space: nowrap;
  }
  .divider {
    position: absolute; left: 381px; top: 93px;
    width: 2px; height: 209px; background: var(--accent);
  }
  .details { position: absolute; left: 408px; top: 90px; color: var(--ink); }
  .person-name {
    font-weight: 700; font-size: 25px; color: var(--accent); line-height: 30px;
  }
  .job-title { font-size: 18px; line-height: 24px; margin-bottom: 14px; }
  .address { font-size: 18px; line-height: 28px; margin-bottom: 8px; }
  .contact-row {
    display: flex; align-items: center; gap: 8px;
    font-size: 18px; line-height: 27.5px;
  }
  .contact-row svg { width: 15px; height: 15px; flex: none; }
</style>
</head>
<body>
<div class="canvas">
  <section class="card card-front">
    <div class="front-brand">Coralvale Meat Traders</div>
  </section>

  <section class="card card-back">
    <div class="back-brand">Coralvale Meat Traders</div>
    <div class="divider"></div>
    <div class="details">
      <div class="person-name">DANIEL HARWOOD</div>
      <div class="job-title">Managing Director</div>
      <div class="address">Your address, City<br>State, Zip 1234</div>
      <div class="contact-row">
        <svg viewBox="0 0 16 16" aria-hidden="true"><path fill="#8b1a1a" d="M1 6c0-2 3-3 7-3s7 1 7 3v1h-3V6H4v1H1zM4 8h8l2 5H2z"/></svg>
        <span>123 456 789</span>
      </div>
      <div class="contact-row">
        <svg viewBox="0 0 16 16" aria-hidden="true"><path fill="#8b1a1a" d="M1 6l7-5 7 5v9H1z"/><path fill="#fff" d="M2.5 7l5.5 4 5.5-4v6.5h-11z"/></svg>
        <span>info@yourgmail.com</span>
      </div>
      <div class="contact-row">
        <svg viewBox="0 0 16 16" aria-hidden="true"><circle cx="8" cy="8" r="7" fill="#8b1a1a"/><path fill="#fff" d="M5 4c2 0 3 2 2 3S4 8 4 10 6 13 6 14C3 13 2 10 3 7zM10 9c2 0 3 1 2 3l-2 1z"/></svg>
        <span>www.yourwebsite.com</span>
      </div>
    </div>
  </section>
</div>
</body>
</html>
```